Brodnicka and Associates Letterhead and Business Cards
Changes to ph #s only - same logo and design as previously used
Brodnicka and Associates Letterhead and Business Cards - Corporate Services
Creative Brief
Traditional
Halina Brodnicka
NA
Office: 610-555-0147
Hal@BrodnickaPartners.example
PixelMorrow PixelMorrow
Kindly Check #110 and #111 with letterhead thanks
hbx4172 hbx4172
I already responded to this. I like #97 best but before making that final decision - want to see how the design looks in the letterhead
I like #97 beast but before making that choice will need to see how the design looks on letterhead as I want the business cards and letterhead to have the same look

```html
<!DOCTYPE html>
<html lang="en">
<head>
<meta charset="utf-8">
<title>Brodnicka and Associates – Business Card</title>
<link rel="stylesheet" href="https://fonts.googleapis.com/css2?family=Open+Sans:wght@400;600&display=swap">
<style>
  :root {
    --backdrop: #d9d9d9;
    --card-white: #ffffff;
    --card-dark: #2c3a33;
    --brand-green: #1ea04b;
    --brand-blue: #2f7bc4;
    --accent-purple: #9b2fa8;
    --ink: #3a3a3a;
    --ink-soft: #6b6b6b;
  }
  * { box-sizing: border-box; margin: 0; padding: 0; }
  html, body {
    width: 1200px; height: 895px; overflow: hidden;
    background: var(--backdrop);
    font-family: "Open Sans", Arial, sans-serif;
  }
  .stage {
    position: relative; width: 1200px; height: 895px;
    display: flex; align-items: center; justify-content: center; gap: 50px;
  }
  .card {
    position: relative; width: 525px; height: 300px;
    box-shadow: 0 6px 18px rgba(0,0,0,.18);
    overflow: hidden;
  }
  /* Front */
  .card--front { background: var(--card-white); }
  .brand {
    position: absolute; top: 62px; left: 0; right: 0;
    display: flex; align-items: center; justify-content: center; gap: 10px;
  }
  .brand__mark {
    width: 18px; height: 18px; background: var(--brand-green);
  }
  .brand__name {
    font-weight: 600; font-size: 24px; line-height: 1;
    color: var(--brand-green);
  }
  .person {
    position: absolute; top: 142px; left: 34px;
    display: flex; align-items: center; gap: 10px;
  }
  .person__name { font-size: 21px; font-weight: 600; color: var(--ink); }
  .person__divider { width: 2px; height: 24px; background: var(--accent-purple); }
  .person__title { font-size: 15px; color: var(--accent-purple); }
  .address {
    position: absolute; top: 180px; left: 34px;
    font-size: 12.5px; color: var(--ink-soft);
  }
  .contact-band {
    position: absolute; left: 0; top: 210px; width: 500px; height: 62px;
    background: var(--brand-green);
    border-radius: 0 31px 31px 0;
    color: #fff; font-size: 12.5px;
  }
  .contact-band__phones {
    position: absolute; left: 34px; top: 10px;
    display: flex; gap: 34px;
  }
  .contact-item { display: flex; align-items: center; gap: 6px; }
  .contact-item svg { width: 12px; height: 12px; fill: #fff; }
  .contact-band__email { position: absolute; right: 26px; bottom: 10px; }
  /* Back */
  .card--back { background: var(--card-dark); }
  .web-pill {
    position: absolute; top: 26px; left: 0;
    height: 28px; padding: 0 22px 0 26px;
    background: var(--brand-blue);
    border-radius: 0 14px 14px 0;
    color: #e8f1fb; font-size: 12.5px; line-height: 28px;
  }
</style>
</head>
<body>
<main class="stage">
  <section class="card card--front" aria-label="Business card front">
    <div class="brand">
      <span class="brand__mark" aria-hidden="true"></span>
      <span class="brand__name">Brodnicka &amp; Associates</span>
    </div>
    <div class="person">
      <span class="person__name">Halina Brodnicka</span>
      <span class="person__divider"></span>
      <span class="person__title">President &amp; CEO</span>
    </div>
    <p class="address">240 Harrow Lane, 18th Floor, Media PA</p>
    <div class="contact-band">
      <div class="contact-band__phones">
        <span class="contact-item">
          <svg viewBox="0 0 24 24" aria-hidden="true"><path d="M6.6 10.8a15.1 15.1 0 0 0 6.6 6.6l2.2-2.2a1 1 0 0 1 1-.25 11.4 11.4 0 0 0 3.6.57 1 1 0 0 1 1 1V20a1 1 0 0 1-1 1A17 17 0 0 1 3 4a1 1 0 0 1 1-1h3.5a1 1 0 0 1 1 1c0 1.25.2 2.450.57 3.57a1 1 0 0 1-.25 1z"/></svg>
          610-555-0147
        </span>
        <span class="contact-item">
          <svg viewBox="0 0 24 24" aria-hidden="true"><path d="M6.6 10.8a15.1 15.1 0 0 0 6.6 6.6l2.2-2.2a1 1 0 0 1 1-.25 11.4 11.4 0 0 0 3.6.57 1 1 0 0 1 1 1V20a1 1 0 0 1-1 1A17 17 0 0 1 3 4a1 1 0 0 1 1-1h3.5a1 1 0 0 1 1 1c0 1.25.2 2.45.57 3.57a1 1 0 0 1-.25 1z"/></svg>
          610-555-0182
        </span>
      </div>
      <span class="contact-band__email">Hal@BrodnickaPartners.example</span>
    </div>
  </section>

  <section class="card card--back" aria-label="Business card back">
    <div class="web-pill">www.BrodnickaPartners.example</div>
  </section>
</main>
</body>
</html>
```